Marlow Estate Group (Real Estate and Investment)

A high end, clean design.
We are a real estate company with sales, asset management and investment divisions. We want to use a black and white scheme which is really high end feel. The back of the card can just be the logo (black background with the white writing) as we will probably emboss this when we print)

Target Market(s)

High level investors, high end houses for sale

Industry/Entity Type

Business

Contact Information for Business Card

Name, position, phone number and email address
Ben Marlow, Managing Director, 0438926057 and ben@marlowestate.com.au

Requirements
Must have
• Back of the card to be the black background with the white writing (as per the attached images). Would like the capacity to emboss the writing and logo

```html
<!DOCTYPE html>
<html lang="en">
<head>
<meta charset="utf-8">
<title>Marlow Estate Group – Business Card</title>
<link href="https://fonts.googleapis.com/css2?family=Montserrat:wght@300;400;600;700&family=Roboto:wght@400&display=swap" rel="stylesheet">
<style>
  :root {
    --backdrop: #e6e4e1;
    --card-black: #141414;
    --card-white: #fbfbfa;
    --ink: #111111;
    --ink-soft: #3a3a3a;
    --band-grey: #8a8a8a;
    --emboss: #2e2e2e;
  }
  * { box-sizing: border-box; margin: 0; padding: 0; }
  html, body {
    width: 1200px; height: 716px; overflow: hidden;
    background: var(--backdrop);
  }
  .canvas {
    position: relative; width: 1200px; height: 716px;
    display: flex; align-items: center; justify-content: center; gap: 60px;
  }
  .card {
    position: relative; width: 500px; height: 306px;
    box-shadow: 0 6px 18px rgba(0,0,0,0.18);
  }

  /* Back of card */
  .card-back {
    background: var(--card-black);
    display: flex; flex-direction: column; align-items: center; justify-content: center; gap: 18px;
  }
  .card-back .brand-mark {
    width: 92px; height: 92px; border: 2px solid var(--emboss); border-radius: 50%;
  }
  .card-back .brand-name {
    font-family: "Montserrat", sans-serif; font-weight: 600;
    font-size: 26px; letter-spacing: 0.5px; text-transform: uppercase;
    color: var(--emboss);
  }

  /* Front of card */
  .card-front { background: var(--card-white); overflow: hidden; }
  .edge-band {
    position: absolute; left: 0; top: 0; bottom: 0; width: 36px;
    background: var(--card-black);
  }
  .edge-band::after {
    content: ""; position: absolute; right: -6px; top: 0; bottom: 0; width: 6px;
    background: var(--band-grey);
  }
  .brand {
    position: absolute; right: 34px; top: 58px;
    display: flex; align-items: center; gap: 16px;
  }
  .brand-mark {
    width: 58px; height: 58px; border: 1.5px solid var(--ink); border-radius: 50%;
  }
  .brand .brand-name {
    font-family: "Montserrat", sans-serif; font-weight: 600;
    font-size: 19px; line-height: 1.1; text-transform: uppercase; color: var(--ink);
    width: 118px;
  }
  .person {
    position: absolute; left: 78px; top: 150px;
    font-family: "Montserrat", sans-serif; color: var(--ink);
  }
  .person-name { font-size: 19px; font-weight: 300; letter-spacing: 0.5px; text-transform: uppercase; }
  .person-name strong { font-weight: 700; }
  .person-role { font-family: "Roboto", sans-serif; font-size: 11px; color: var(--ink-soft); margin-top: 1px; }
  .contacts {
    list-style: none; margin-top: 12px;
    font-family: "Roboto", sans-serif; font-size: 14px; color: var(--ink);
  }
  .contacts li { display: flex; align-items: center; gap: 10px; height: 20px; }
  .contacts svg { width: 13px; height: 13px; flex: none; }
</style>
</head>
<body>
<main class="canvas">
  <section class="card card-back" aria-label="Card back">
    <span class="brand-mark"></span>
    <span class="brand-name">Marlow Estate Group</span>
  </section>

  <section class="card card-front" aria-label="Card front">
    <div class="edge-band"></div>
    <div class="brand">
      <span class="brand-mark"></span>
      <span class="brand-name">Marlow Estate Group</span>
    </div>
    <div class="person">
      <h1 class="person-name">Ben <strong>Marlow</strong></h1>
      <p class="person-role">Managing Director</p>
      <ul class="contacts">
        <li>
          <svg viewBox="0 0 16 16" aria-hidden="true"><path fill="currentColor" d="M2 5c0-2 2-3 6-3s6 1 6 3v1h-3V5H5v1H2zM4 7h8l2 7H2z"/></svg>
          0438926057
        </li>
        <li>
          <svg viewBox="0 0 16 16" aria-hidden="true"><rect x="1" y="3" width="14" height="10" fill="currentColor"/><path d="M1.5 3.5L8 9l6.5-5.5" stroke="#fff" stroke-width="1.2" fill="none"/></svg>
          ben@marlowestate.com.au
        </li>
        <li>
          <svg viewBox="0 0 16 16" aria-hidden="true"><circle cx="8" cy="8" r="7" fill="currentColor"/><path d="M1 8h14M8 1c-3 3-3 11 0 14M8 1c3 3 3 11 0 14" stroke="#fff" stroke-width="0.9" fill="none"/></svg>
          www.marlowestate.com.au
        </li>
      </ul>
    </div>
  </section>
</main>
</body>
</html>
```